Pantry Barn EPP Mailer

This card will be mailed to local communities to make people aware of the ALL the Products - particularly local food - offered at Pantry Barn of Willowbrook. On the attached copy, the content in BOLD should be emphasized. Not all of the photos need to be utilized, but wanted to provide an assortment that shows off food and merchandise. Please note - this card is 8 in. x 6.5 inches and MUST be laid out to conform the the Each Porch Post format attached - with mailing and postage spaces left in the areas indicated on one side.

```html
<!DOCTYPE html>
<html lang="en">
<head>
<meta charset="utf-8">
<title>Pantry Barn of Willowbrook – Mailer</title>
<link href="https://fonts.googleapis.com/css2?family=Catamaran:wght@400;600;700&display=swap" rel="stylesheet">
<style>
:root{
  --page:#e8e4dd;
  --cream:#fdfbe1;
  --green-deep:#3b9636;
  --green:#4caa3b;
  --green-light:#7cc143;
  --green-bar:#5cb43e;
  --orange:#f7b42c;
  --butter:#fff5b8;
  --ink-green:#2f7f2c;
}
*{box-sizing:border-box;margin:0;padding:0}
html,body{width:1200px;height:566px;overflow:hidden;background:var(--page);font-family:'Catamaran',sans-serif}
.card{position:absolute;background:var(--cream);overflow:hidden;box-shadow:0 2px 6px rgba(0,0,0,.18)}
.card--front{left:31px;top:49px;width:541px;height:445px}
.card--back{left:628px;top:53px;width:538px;height:440px}

.brand{position:absolute;color:var(--green);font-weight:400;line-height:1}
.brand-rule{position:absolute;background:var(--green);}
.front-brand{left:22px;top:22px;font-size:17px;line-height:17px}
.front-rule{left:9px;top:61px;width:164px;height:5px}

.bubble{position:absolute;background:var(--green);color:var(--butter);font-weight:600;font-size:8.5px;line-height:9px;text-align:center;display:flex;align-items:center;justify-content:center;border-radius:50%}
.bubble::after{content:"";position:absolute;width:0;height:0;border:5px solid transparent}
.b-open{left:173px;top:10px;width:48px;height:36px;background:var(--green-light)}
.b-open::after{left:2px;bottom:-6px;border-top-color:var(--green-light);border-left-color:var(--green-light)}
.b-family{left:227px;top:10px;width:57px;height:33px;border-radius:45%}
.b-family::after{right:4px;bottom:-6px;border-top-color:var(--green);border-right-color:var(--green)}
.b-kind{left:287px;top:17px;width:41px;height:46px;background:var(--green-light)}
.b-kind::after{left:16px;bottom:-8px;border-top-color:var(--green-light)}
.b-local{left:200px;top:51px;width:91px;height:18px;border-radius:10px}
.b-local::after{left:-5px;top:2px;border-right-color:var(--green);border-top-color:var(--green)}

.band-deep{position:absolute;left:0;top:75px;width:541px;height:152px;background:linear-gradient(90deg,var(--green-deep),var(--green) 70%)}
.band-light{position:absolute;left:0;top:227px;width:541px;height:174px;background:var(--green-light)}
.features-bar{position:absolute;left:0;top:91px;width:292px;height:19px;background:var(--green-light);clip-path:polygon(0 0,100% 0,94% 100%,0 100%);color:#fff;font-weight:600;font-size:10px;line-height:19px;padding-left:36px}
.features{position:absolute;left:28px;top:118px;list-style:none}
.features li{display:flex;align-items:center;height:24.5px;color:var(--orange);font-weight:700;font-size:10.5px}
.icon-slot{width:52px;height:14px;margin-right:18px;border-radius:4px;background:var(--orange);opacity:.85}

.photo{position:absolute}
.front-photo{left:252px;top:0;width:289px;height:445px;
  background:linear-gradient(160deg,#9aa38c 0%,#7a6a52 25%,#c98d4f 45%,#b2333a 60%,#a88352 75%,#e6a66b 90%,#5e4a33 100%);
  clip-path:polygon(77px 0,100% 0,100% 100%,0 100%,0 227px,77px 227px)}

.body-copy{position:absolute;left:25px;top:243px;width:250px;color:#fff;font-size:8.3px;line-height:10.3px}
.body-copy p+p{margin-top:6px}
.body-copy strong{font-weight:700}
.day-bar{position:absolute;left:0;top:318px;width:207px;height:19px;background:var(--green);clip-path:polygon(0 0,100% 0,93% 100%,0 100%);color:#fff;font-weight:600;font-size:8.6px;line-height:20px;padding-left:31px}
.pin{position:absolute;left:22px;top:352px;width:18px;height:30px}
.address{position:absolute;left:45px;top:351px;color:var(--butter);font-weight:700;font-size:8.6px;line-height:11.5px}
.social{position:absolute;left:176px;top:353px;display:flex;gap:3px}
.social span{width:21px;height:21px;border-radius:50%;border:2px solid var(--green)}
.online{position:absolute;left:175px;top:377px;color:var(--green);font-size:7.2px;font-weight:600}
.contact{position:absolute;left:16px;top:419px;display:flex;align-items:center;gap:6px;color:var(--ink-green);font-size:8.5px;font-weight:600}
.contact svg{display:block}
.contact .web{margin-left:6px}

.back-brand{left:14px;top:23px;font-size:10px;line-height:10px}
.back-rule{left:5px;top:48px;width:107px;height:3px}
.back-address{position:absolute;left:120px;top:19px;color:var(--green);font-size:7.4px;line-height:11.4px}
.stamp{position:absolute;left:449px;top:15px;width:71px;height:71px;border:1.5px solid var(--green)}
.mail-box{position:absolute;left:259px;top:247px;width:184px;height:70px;border:1.5px solid var(--green)}
.strips{position:absolute;left:0;top:0;width:229px;height:440px}
</style>
</head>
<body>

<section class="card card--front">
  <div class="band-deep"></div>
  <div class="band-light"></div>

  <div class="brand front-brand">Pantry Barn<br>of Willowbrook</div>
  <div class="brand-rule front-rule"></div>

  <div class="bubble b-open">Open<br>7 Days!</div>
  <div class="bubble b-family">Family-Run</div>
  <div class="bubble b-kind">Kind<br>Service</div>
  <div class="bubble b-local">Locally Focused</div>

  <div class="photo front-photo" role="img" aria-label="Photo of the shop interior: shelves of pantry goods and baskets of fresh apples, peaches, tomatoes and avocados on wooden crates"></div>

  <div class="features-bar">Pantry Barn of Willowbrook&nbsp; proudly features:</div>
  <ul class="features">
    <li><span class="icon-slot" role="img" aria-label="Produce, meat and cheese icons"></span>Local Produce, Meat &amp; Cheese</li>
    <li><span class="icon-slot" role="img" aria-label="Bread and sweets icons"></span>Local Breads &amp; Sweets</li>
    <li><span class="icon-slot" role="img" aria-label="Globe and bowl icons"></span>International Foods</li>
    <li><span class="icon-slot" role="img" aria-label="Kitchen tool, cup and gift icons"></span>Kitchen • Home • Gift Items</li>
  </ul>

  <div class="body-copy">
    <p>Discover our many <strong>Regional Food Items.</strong><br>Choosing locally grown/produced, healthy food<br>benefits you, your neighbors &amp; our planet. We like that.</p>
    <p>Please stop in and see the changes we have in<br>store...with more to come!</p>
  </div>

  <div class="day-bar">Make A Day of It in Willowbrook!</div>

  <svg class="pin" viewBox="0 0 18 30" aria-hidden="true"><path d="M9 0C4 0 0 4 0 9c0 7 9 21 9 21s9-14 9-21C18 4 14 0 9 0z" fill="var(--green)"/><circle cx="9" cy="9" r="3.5" fill="var(--green-light)"/></svg>
  <div class="address">Corner of Elm &amp; Mill Streets<br>212 Elm Street, Willowbrook<br>555 014-2290</div>
  <div class="social"><span></span><span></span></div>
  <div class="online">join us online</div>

  <div class="contact">
    <svg width="15" height="11" viewBox="0 0 15 11" aria-hidden="true"><rect x=".75" y=".75" width="13.5" height="9.5" fill="none" stroke="var(--green)" stroke-width="1.5"/><path d="M1 1l6.5 5L14 1" fill="none" stroke="var(--green)" stroke-width="1.5"/></svg>
    <span>pantrybarn@valleymail.net</span>
    <svg class="web" width="9" height="12" viewBox="0 0 9 12" aria-hidden="true"><path d="M0 0l9 7H5l2 5-2 .5-2-5-3 3z" fill="var(--green)"/></svg>
    <span>www.PBOW.net</span>
  </div>
</section>

<section class="card card--back">
  <div class="brand back-brand">Pantry Barn<br>of Willowbrook</div>
  <div class="brand-rule back-rule"></div>
  <div class="back-address">Corner of Elm &amp; Mill Streets<br>212 Elm Street, Willowbrook<br>555 014-2290</div>

  <div class="stamp"></div>
  <div class="mail-box"></div>

  <svg class="strips" viewBox="0 0 229 440" aria-hidden="false">
    <defs>
      <linearGradient id="g-bake" x1="0" x2="1"><stop offset="0" stop-color="#8a6a45"/><stop offset="1" stop-color="#b79a6a"/></linearGradient>
      <linearGradient id="g-pillow" x1="0" x2="1"><stop offset="0" stop-color="#2f8fb5"/><stop offset=".6" stop-color="#e6dcc6"/><stop offset="1" stop-color="#c9a25a"/></linearGradient>
      <linearGradient id="g-bread" x1="0" x2="1"><stop offset="0" stop-color="#6d5640"/><stop offset=".5" stop-color="#c39a62"/><stop offset="1" stop-color="#8b7a66"/></linearGradient>
      <linearGradient id="g-jar" x1="0" y1="0" x2="0" y2="1"><stop offset="0" stop-color="#5b3a2a"/><stop offset=".45" stop-color="#c7a25a"/><stop offset="1" stop-color="#e38a45"/></linearGradient>
    </defs>
    <polygon role="img" aria-label="Photo of baked goods wrapped on a shelf" points="0,64 229,64 229,109 0,134" fill="url(#g-bake)"/>
    <polygon role="img" aria-label="Photo of decorative pillows on display shelves" points="0,139 229,112 229,213 0,199" fill="url(#g-pillow)"/>
    <polygon role="img" aria-label="Photo of packaged loaves of local bread" points="0,203 229,218 229,265 0,300" fill="url(#g-bread)"/>
    <polygon role="img" aria-label="Photo of international sauces, jars and a basket of peaches" points="0,305 229,272 229,440 0,440" fill="url(#g-jar)"/>
    <rect x="104" y="384" width="125" height="56" fill="var(--green-light)"/>
  </svg>
</section>

</body>
</html>
```